Flyer design for Trail Beside Outback Trips

We need a new flyer for our tour business. Sketch hive produced a great flyer for us 4 years ago but it is time to update. We have had a price increase that needs to be reflected but we have noticed an issue with our current marketing.
Our tour is a "tagalong" tour which means you follow in your own vehicle. Unfortunately most people associate "tagalong" with 4wd (Four wheel drive vehicles). This is not the case for our tour which can be done in ANY type of vehicle. We need to get across at first glance that this tour is available to all vehicle types. We also need to stress that there is NOT MUCH DRIVING. We cover around 20km total of very easy driving. We go from point of interest to point of interest.
We want our customers to feel that this tour will be a better option than selecting a bus type tour because they use their own vehicle. Our option is also MUCH cheaper than bus options but provides a premium product. It's "cheap" but not cheap if you understand.
I will upload our previous flyer so you have an idea of what we do and how we have been presenting it. We are currently single sided DL but do not mind if we go into double sided DL if you feel that will enable you to share more information. Our price is $50 and half price for kids (as per old flyer)
Some things to remember when trying to appeal to our customer:
Choose a design that clearly communicates that our tagalong tour is suitable for all types of vehicles. For example, "Vehicle-Friendly Tagalong Tour" or "All-Vehicle Tagalong Tour".
Use clear language: Avoid using terms like "off-road" or "4x4" that may imply that our tour is only suitable for certain types of vehicles. Instead, use language that is inclusive and clearly communicates that all vehicles are welcome.
Include photos and videos of a variety of vehicles: This will show potential customers that our tagalong tour is not limited to four-wheel drive vehicles and that any type of vehicle can participate.
Highlight the benefits of a tagalong tour over a bus tour: Emphasise the flexibility and freedom that a tagalong tour offers, as well as the opportunity to explore off-the-beaten-path destinations that are not accessible by bus.
By incorporating these elements into your product presentation, you can avoid confusion and clearly communicate that our tagalong tour is suitable for any type of vehicle, while also highlighting the unique benefits of this type of tour.
Along with the emphasis on all vehicles you need to be clear about what we offer on the tour.
- The excitement of an opal mine tour with an award winning guide and opal miner.
- The wonder of an underground home and discovering how people live in an underground environment.
- Driving through the opal mining area for a close up view of the field.
- Our EXCLUSIVE opal cutting and polishing demonstration.
- The adventure of looking for your own opal.
For further information visit our web site "http://trailbeside.outbackway.example". Check our facebook page "https://www.facebook.com/trailbesideoutbacktrips". Search Seekora for "Coober Pedy", Trail beside Outback Coober Pedy" or "Coober Pedy Opal mining" to source images of our town and opals.
PLEASE ALSO FIND SOMEWHERE TO SAY "FREE UNPOWERED CAMPING AT TALMO'S WITH ALL TOURS AS WELL AS DISCOUNTS ON POWERED CAMPING" and make this stand out somehow. (http://stay-belowgrid.example.au)

Target Market(s)

18 to 80

Industry/Entity Type

Tourism

Font styles to use
Serif

Colors

Designer to choose colors to be used in the design.

Requirements
Must have
• Eye catching images and attention grabbing headlines
Nice to have
• Modern design.
Should not have
• References to 4wd or buses.

```html
<!DOCTYPE html>
<html lang="en">
<head>
<meta charset="utf-8">
<title>Tagalong Tour – Trail Beside Outback Trips</title>
<link rel="stylesheet" href="https://fonts.googleapis.com/css2?family=Passion+One:wght@400;700&family=Open+Sans:ital,wght@1,400;1,600;1,700;1,800&display=swap">
<style>
  :root{
    --orange:#f47b20;
    --orange-deep:#e8650f;
    --white:#ffffff;
    --ink:#2b2b2b;
    --sky-top:#3d7fc4;
    --sky-low:#b9d3ea;
    --dust:#c9a27c;
    --mine-dark:#4a3a2e;
    --mine-light:#b89a7a;
  }
  *{margin:0;padding:0;box-sizing:border-box}
  html,body{width:778px;height:1200px;overflow:hidden;background:var(--white)}
  .flyer{position:relative;width:778px;height:1200px;overflow:hidden;background:var(--white);font-family:"Open Sans",Arial,sans-serif;color:var(--ink)}
  .splash{position:absolute;left:0;top:0;width:778px;height:1200px}
  .brand{position:absolute;left:12px;top:0;width:86px;height:104px;background:var(--orange);display:flex;flex-direction:column;align-items:center;justify-content:center;gap:6px;color:var(--white);font-family:"Open Sans",sans-serif;font-style:italic;font-weight:700;font-size:11px;text-align:center;line-height:1.15}
  .brand-dot{width:22px;height:22px;border-radius:50%;background:var(--white)}
  .title{position:absolute;left:118px;top:10px;font-family:"Passion One",Impact,sans-serif;font-weight:700;font-size:70px;line-height:1;color:var(--orange);letter-spacing:.5px;transform:skewX(-6deg)}
  .subtitle{position:absolute;z-index:2;right:34px;top:80px;font-family:"Passion One",Impact,sans-serif;font-weight:700;font-size:32px;line-height:1;color:var(--orange);transform:skewX(-8deg)}
  .photo{position:absolute}
  .photo-convoy{left:38px;top:140px;width:720px;height:264px;background:linear-gradient(180deg,var(--sky-top) 0%,var(--sky-low) 48%,var(--dust) 52%,#a97f5a 100%)}
  .photo-mine{left:462px;top:440px;width:300px;height:190px;background:linear-gradient(160deg,var(--mine-light),var(--mine-dark))}
  .photo-guests{left:448px;top:650px;width:300px;height:280px;background:linear-gradient(150deg,#d8c2a6,#8a6d52);transform:rotate(4deg);border:6px solid var(--white);box-shadow:0 2px 8px rgba(0,0,0,.25)}
  .intro{position:absolute;left:32px;top:448px;width:410px;color:var(--white);font-style:italic;font-weight:700;font-size:19.5px;line-height:1.28}
  .intro-mark{position:absolute;left:-4px;top:-38px;font-family:"Passion One",sans-serif;font-size:60px;font-style:normal}
  .features{position:absolute;left:20px;top:672px;width:410px;list-style:none}
  .feature{display:flex;align-items:flex-start;gap:14px;margin-bottom:22px;font-style:italic;font-size:14.5px;line-height:1.3}
  .feature svg{flex:none;width:28px;height:28px;margin-top:2px}
  .feature .hl{color:var(--orange);font-weight:700}
  .price{position:absolute;left:578px;top:830px;width:164px;height:164px;border-radius:50%;background:var(--orange);border:4px solid var(--white);color:var(--white);display:flex;flex-direction:column;align-items:center;justify-content:center;text-align:center;font-style:italic}
  .price-amount{font-family:"Passion One",sans-serif;font-weight:700;font-size:52px;line-height:.9;font-style:normal}
  .price-unit{font-weight:800;font-size:19px}
  .price-note{font-size:10px}
  .contact{position:absolute;left:22px;top:1058px;font-size:12px;line-height:1.45;font-style:italic}
  .contact-web{display:flex;align-items:center;gap:6px;font-weight:800;font-size:14px;font-style:normal}
  .camping{position:absolute;left:478px;top:1100px;width:280px;color:var(--white);font-style:italic;font-weight:600;font-size:13px;line-height:1.3;text-align:center}
</style>
</head>
<body>
<main class="flyer">
  <svg class="splash" viewBox="0 0 778 1200" aria-hidden="true">
    <path fill="var(--orange)" d="M20 156 L60 128 L140 134 L300 126 L470 132 L640 124 L770 132 L774 260 L768 420 L700 430 L560 424 L400 432 L200 426 L60 432 L28 400 L34 300 Z"/>
    <path fill="var(--orange)" d="M0 412 L120 396 L300 408 L520 398 L778 410 L778 640 L700 650 L600 636 L470 646 L420 610 L300 600 L180 614 L60 602 L0 612 Z"/>
    <path fill="var(--orange-deep)" d="M0 580 L90 596 L200 582 L330 598 L440 584 L440 612 L300 604 L160 618 L40 606 L0 616 Z"/>
    <path fill="var(--orange)" d="M460 1090 L560 1080 L690 1088 L778 1078 L778 1168 L700 1176 L580 1170 L470 1178 L456 1140 Z"/>
  </svg>

  <div class="brand"><span class="brand-dot"></span><span>Trail Beside</span></div>
  <h1 class="title">Tagalong Tour</h1>
  <p class="subtitle">Vehicle-Friendly</p>

  <div class="photo photo-convoy" role="img" aria-label="Cars and a motorbike of different kinds parked together on the open opal field under a blue sky"></div>

  <p class="intro"><span class="intro-mark">“</span>A unique tag-along journey through Coober Pedy. Enjoy a tour from the comfort of your own car as our experienced guide takes you through a “day in the life” of a Coober Pedy miner.</p>

  <div class="photo photo-mine" role="img" aria-label="Tour guests in hard hats inside an underground opal mine"></div>
  <div class="photo photo-guests" role="img" aria-label="Collage of happy tour guests in hard hats on the tour"></div>

  <ul class="features">
    <li class="feature"><svg viewBox="0 0 28 28"><rect width="28" height="28" rx="6" fill="var(--orange)"/><path d="M8 14.5l4 4 8-9" stroke="#fff" stroke-width="3" fill="none" stroke-linecap="round" stroke-linejoin="round"/></svg><span>The excitement of an opal mine tour with an award winning guide and opal miner. and Try our <span class="hl">EXCLUSIVE opal cutting</span> and polishing demonstration.</span></li>
    <li class="feature"><svg viewBox="0 0 28 28"><rect width="28" height="28" rx="6" fill="var(--orange)"/><path d="M8 14.5l4 4 8-9" stroke="#fff" stroke-width="3" fill="none" stroke-linecap="round" stroke-linejoin="round"/></svg><span>The wonder of an underground home and discovering how people live in an underground environment.</span></li>
    <li class="feature"><svg viewBox="0 0 28 28"><rect width="28" height="28" rx="6" fill="var(--orange)"/><path d="M8 14.5l4 4 8-9" stroke="#fff" stroke-width="3" fill="none" stroke-linecap="round" stroke-linejoin="round"/></svg><span>Driving through the opal mining area for a close up view of the field. Its an adventure of looking for your own opal</span></li>
    <li class="feature"><svg viewBox="0 0 28 28"><rect width="28" height="28" rx="6" fill="var(--orange)"/><path d="M8 14.5l4 4 8-9" stroke="#fff" stroke-width="3" fill="none" stroke-linecap="round" stroke-linejoin="round"/></svg><span>Any type of vehicle can participate. Flexible / Freedom / Cheaper than any other mode of experience</span></li>
    <li class="feature"><svg viewBox="0 0 28 28"><rect width="28" height="28" rx="6" fill="var(--orange)"/><path d="M8 14.5l4 4 8-9" stroke="#fff" stroke-width="3" fill="none" stroke-linecap="round" stroke-linejoin="round"/></svg><span>Easy Driving.We cover around 20km in total</span></li>
  </ul>

  <div class="price">
    <span class="price-amount">$50</span>
    <span class="price-unit">Per Person</span>
    <span class="price-note">(Kid half price)</span>
  </div>

  <div class="contact">
    <p>Phone: 08 5550 1427</p>
    <p>trail@beside.example</p>
    <p class="contact-web"><svg width="16" height="16" viewBox="0 0 16 16"><circle cx="8" cy="8" r="7" fill="none" stroke="var(--ink)" stroke-width="1.5"/><ellipse cx="8" cy="8" rx="3" ry="7" fill="none" stroke="var(--ink)" stroke-width="1.2"/><line x1="1" y1="8" x2="15" y2="8" stroke="var(--ink)" stroke-width="1.2"/></svg>www.stay-belowgrid.example.au</p>
  </div>

  <p class="camping">Free unpowered camping at Talmo's with all Tours as well as discounts on powered camping</p>
</main>
</body>
</html>
```